Business Card + Letterhead Design for KESTOVA TRADING INC.

We already have a logo; now we need a business card + letterhead. We import and distribute flags and souvenirs with an emphasis on soccer related memorabilia. We target various ethnic markets and sporting goods stores. "International Souvenirs"

```html
<!DOCTYPE html>
<html lang="en">
<head>
<meta charset="utf-8">
<title>Kestova Trading – Business Card</title>
<link rel="stylesheet" href="https://fonts.googleapis.com/css2?family=Arimo:wght@400;700&family=Cinzel:wght@700&display=swap">
<style>
  :root {
    --page: #ffffff;
    --card: #000000;
    --card-edge: #8a8a8a;
    --tab: #fbfbfb;
    --brand-red: #7a1414;
    --banner-red: #6e0c0c;
    --ink-light: #ffffff;
    --ink-soft: #e6e6e6;
    --icon: #b8b8b8;
    --divider: #555555;
  }
  * { margin: 0; padding: 0; box-sizing: border-box; }
  html, body { width: 1051px; height: 1200px; overflow: hidden; background: var(--page); }
  body { position: relative; font-family: "Arimo", Arial, sans-serif; }

  .card {
    position: absolute;
    background: var(--card);
    border: 1px solid var(--card-edge);
  }
  .card--front { left: 98px; top: 72px; width: 853px; height: 508px; }
  .card--back  { left: 102px; top: 613px; width: 852px; height: 507px; }

  .brand-tab {
    position: absolute;
    background: var(--tab);
    display: flex;
    align-items: center;
    justify-content: center;
  }
  .card--front .brand-tab {
    left: 127px; top: -1px; width: 598px; height: 341px;
    border-radius: 0 0 24px 24px;
    padding-top: 170px;
  }
  .card--back .brand-tab {
    left: -1px; top: 64px; width: 292px; height: 111px;
    border-radius: 0 18px 18px 0;
  }

  .brand {
    display: flex;
    align-items: center;
    color: var(--brand-red);
    font-family: "Arimo", Arial, sans-serif;
    font-weight: 700;
  }
  .brand__dot { border-radius: 50%; background: var(--brand-red); flex: none; }
  .brand__name { display: flex; flex-direction: column; line-height: 1; }
  .brand__word { text-transform: lowercase; }
  .brand__sub { letter-spacing: 0.5em; }

  .brand--large .brand__dot { width: 52px; height: 52px; margin-right: 34px; }
  .brand--large .brand__word { font-size: 72px; }
  .brand--large .brand__sub { font-size: 24px; margin-top: 6px; padding-left: 4px; }

  .brand--small .brand__dot { width: 24px; height: 24px; margin-right: 16px; }
  .brand--small .brand__word { font-size: 34px; }
  .brand--small .brand__sub { font-size: 12px; margin-top: 3px; padding-left: 2px; }

  .holder {
    position: absolute;
    left: 360px; top: 100px; width: 514px;
    text-align: center;
    color: var(--ink-light);
  }
  .holder__name {
    font-family: "Cinzel", "Times New Roman", serif;
    font-weight: 700;
    font-size: 30px;
    letter-spacing: 0.02em;
  }
  .holder__company {
    font-size: 21px;
    color: var(--ink-soft);
    margin-top: 2px;
  }

  .contact {
    position: absolute;
    top: 357px;
    list-style: none;
    color: var(--ink-light);
    font-size: 25px;
  }
  .contact li { display: flex; align-items: center; height: 35px; }
  .contact svg { width: 30px; height: 30px; margin-right: 8px; flex: none; }
  .contact--phone { left: 65px; }
  .contact--web { left: 435px; }

  .contact-divider {
    position: absolute;
    left: 380px; top: 353px;
    width: 1px; height: 73px;
    background: var(--divider);
  }

  .tagline {
    position: absolute;
    left: 173px; top: 448px;
    width: 527px; height: 56px;
    background: var(--banner-red);
    color: var(--ink-light);
    font-size: 27px;
    display: flex; align-items: center; justify-content: center;
  }
</style>
</head>
<body>

<section class="card card--front">
  <div class="brand-tab">
    <div class="brand brand--large">
      <span class="brand__dot"></span>
      <span class="brand__name">
        <span class="brand__word">kestova</span>
        <span class="brand__sub">TRADING</span>
      </span>
    </div>
  </div>
</section>

<section class="card card--back">
  <div class="brand-tab">
    <div class="brand brand--small">
      <span class="brand__dot"></span>
      <span class="brand__name">
        <span class="brand__word">kestova</span>
        <span class="brand__sub">TRADING</span>
      </span>
    </div>
  </div>

  <div class="holder">
    <p class="holder__name">Daniel Morrow</p>
    <p class="holder__company">KESTOVA TRADING INC.</p>
  </div>

  <ul class="contact contact--phone">
    <li>
      <svg viewBox="0 0 30 30" aria-hidden="true"><circle cx="15" cy="15" r="13" fill="none" stroke="var(--icon)" stroke-width="1.6"/><path d="M10 8c1-1 2-1 3 0l1.5 2.5c.4.8 0 1.5-.7 2l-1 .7c.8 2 2.3 3.5 4.2 4.3l.8-1c.5-.6 1.2-1 2-.6L22 17.5c1 .8 1 2 0 3-2 2-4.5 1.5-7.5-1.2S8.5 12 9 9.5z" fill="var(--icon)"/></svg>
      <span>: (555) 201-3380</span>
    </li>
    <li>
      <svg viewBox="0 0 30 30" aria-hidden="true"><rect x="9" y="5" width="12" height="8" fill="none" stroke="var(--icon)" stroke-width="1.6"/><rect x="4" y="12" width="22" height="10" rx="2" fill="none" stroke="var(--icon)" stroke-width="1.6"/><rect x="9" y="19" width="12" height="7" fill="var(--card)" stroke="var(--icon)" stroke-width="1.6"/></svg>
      <span>: (555) 418-7720</span>
    </li>
  </ul>

  <div class="contact-divider"></div>

  <ul class="contact contact--web">
    <li>
      <svg viewBox="0 0 30 30" aria-hidden="true"><rect x="3" y="8" width="24" height="15" fill="none" stroke="var(--icon)" stroke-width="1.6"/><path d="M3 8l12 9 12-9M3 23l9-8M27 23l-9-8" fill="none" stroke="var(--icon)" stroke-width="1.6"/></svg>
      <span>: sales@kestovatrading.com</span>
    </li>
    <li>
      <svg viewBox="0 0 30 30" aria-hidden="true"><circle cx="15" cy="15" r="12" fill="none" stroke="var(--icon)" stroke-width="1.6"/><ellipse cx="15" cy="15" rx="5" ry="12" fill="none" stroke="var(--icon)" stroke-width="1.4"/><path d="M3 15h24M5 9h20M5 21h20" stroke="var(--icon)" stroke-width="1.4"/></svg>
      <span>: www.kestovatrading.com</span>
    </li>
  </ul>

  <p class="tagline">“International Flags &amp; Souvenirs”</p>
</section>

</body>
</html>
```